Harrowgate Construction And Masonry Ltd

Black background

Logo - attached

Services (bullet points)
New Builds
Extensions
Refurbishments
Alterations
Brickwork Specialists

Contact details - 01632 960418 or 0791 5530274

Email address - contact@harrowgateconstructionandmasonry.co.uk

Website - www.harrowgateconstructionandmasonry.co.uk

Facebook logo

```html
<!DOCTYPE html>
<html lang="en">
<head>
<meta charset="utf-8">
<title>Harrowgate Construction And Masonry Ltd – Business Card</title>
<link href="https://fonts.googleapis.com/css2?family=Montserrat:wght@500;600;700;800&display=swap" rel="stylesheet">
<style>
  :root {
    --page-bg: #808080;
    --card-dark: #0c1519;
    --brand-green: #00cc6f;
    --line-green: #22e884;
    --ink-dark: #0c1519;
    --text-light: #ffffff;
    --social-blue: #3b5998;
  }
  * { box-sizing: border-box; margin: 0; padding: 0; }
  html, body {
    width: 1200px; height: 900px; overflow: hidden;
    background: var(--page-bg);
    font-family: "Montserrat", sans-serif;
  }
  .business-card {
    position: absolute; left: 100px; top: 97px;
    width: 1000px; height: 706px;
    background: var(--card-dark);
    color: var(--text-light);
  }
  .brand {
    position: absolute; top: 50px; left: 0; width: 100%;
    display: flex; flex-direction: column; align-items: center;
  }
  .brand-square {
    width: 64px; height: 64px; background: var(--brand-green);
    margin-bottom: 36px;
  }
  .brand-name {
    font-weight: 600; color: var(--text-light);
    text-align: center; line-height: 1;
  }
  .brand-name .name-main { display: block; font-size: 46px; letter-spacing: 2px; }
  .brand-name .name-sub { display: block; font-size: 14px; letter-spacing: 0.5px; margin-top: 8px; }

  .services-band {
    position: absolute; top: 278px; left: 0; width: 100%; height: 214px;
    background: var(--brand-green); color: var(--ink-dark);
  }
  .services-title {
    text-align: center; font-weight: 800; font-size: 36px;
    margin-top: 32px; line-height: 1;
  }
  .services-rule {
    width: 806px; height: 2px; background: var(--line-green);
    margin: 10px auto 0;
  }
  .services-row {
    width: 806px; margin: 0 auto;
    display: flex; justify-content: space-between; align-items: center;
    list-style: none; font-weight: 700; font-size: 28px; letter-spacing: 0.5px;
  }
  .services-row.first { margin-top: 14px; }
  .services-row.second { margin-top: 22px; }
  .service { display: flex; align-items: center; gap: 7px; line-height: 1; }
  .tick { width: 22px; height: 22px; flex: none; }

  .contact {
    position: absolute; top: 521px; left: 0; width: 100%;
    text-align: center;
  }
  .contact-title {
    color: var(--brand-green); font-weight: 800; font-size: 29px;
    letter-spacing: 0.5px; line-height: 1;
  }
  .contact-line {
    display: flex; justify-content: center; align-items: center; gap: 7px;
    font-size: 22px; line-height: 1; margin-top: 15px; font-weight: 500;
  }
  .contact-line.phone { font-weight: 600; margin-top: 16px; }
  .contact-icon { width: 21px; height: 21px; flex: none; }
  .social-square {
    position: absolute; left: 873px; top: 637px;
    width: 34px; height: 34px; background: var(--social-blue); border-radius: 2px;
  }
</style>
</head>
<body>
  <div class="business-card">
    <div class="brand">
      <div class="brand-square"></div>
      <div class="brand-name">
        <span class="name-main">HARROWGATE</span>
        <span class="name-sub">CONSTRUCTION AND MASONRY LTD</span>
      </div>
    </div>

    <section class="services-band">
      <h2 class="services-title">OUR SERVICES</h2>
      <div class="services-rule"></div>
      <ul class="services-row first">
        <li class="service"><svg class="tick" viewBox="0 0 22 22"><circle cx="11" cy="11" r="11" fill="#0c1519"/><path d="M6 11.5l3.2 3.2L16 8" fill="none" stroke="#00cc6f" stroke-width="2.6"/></svg>NEW BUILDS</li>
        <li class="service"><svg class="tick" viewBox="0 0 22 22"><circle cx="11" cy="11" r="11" fill="#0c1519"/><path d="M6 11.5l3.2 3.2L16 8" fill="none" stroke="#00cc6f" stroke-width="2.6"/></svg>EXTENSIONS</li>
        <li class="service"><svg class="tick" viewBox="0 0 22 22"><circle cx="11" cy="11" r="11" fill="#0c1519"/><path d="M6 11.5l3.2 3.2L16 8" fill="none" stroke="#00cc6f" stroke-width="2.6"/></svg>ALTERATIONS</li>
      </ul>
      <ul class="services-row second">
        <li class="service"><svg class="tick" viewBox="0 0 22 22"><circle cx="11" cy="11" r="11" fill="#0c1519"/><path d="M6 11.5l3.2 3.2L16 8" fill="none" stroke="#00cc6f" stroke-width="2.6"/></svg>REFURBISHMENTS</li>
        <li class="service"><svg class="tick" viewBox="0 0 22 22"><circle cx="11" cy="11" r="11" fill="#0c1519"/><path d="M6 11.5l3.2 3.2L16 8" fill="none" stroke="#00cc6f" stroke-width="2.6"/></svg>BRICKWORK SPECIALISTS</li>
      </ul>
    </section>

    <section class="contact">
      <h2 class="contact-title">CONTACT DETAILS</h2>
      <p class="contact-line phone">
        <svg class="contact-icon" viewBox="0 0 22 22"><circle cx="11" cy="11" r="11" fill="#00cc6f"/><path d="M7.5 6.5c.8-.5 1.5-.3 1.8.3l.8 1.6c.2.5 0 1-.4 1.3l-.6.4c.6 1.3 1.5 2.2 2.8 2.8l.4-.6c.3-.4.8-.6 1.3-.4l1.6.8c.6.3.8 1 .3 1.8-.6.9-1.6 1.2-2.6.8-2.6-1-4.6-3-5.6-5.6-.4-1 0-2 .8-2.6z" fill="#0c1519"/></svg>
        01632 960418 or 0791 5530274
      </p>
      <p class="contact-line">
        <svg class="contact-icon" viewBox="0 0 22 22"><circle cx="11" cy="11" r="11" fill="#00cc6f"/><rect x="5.5" y="7" width="11" height="8" fill="none" stroke="#0c1519" stroke-width="1.4"/><path d="M5.5 7l5.5 4.5L16.5 7" fill="none" stroke="#0c1519" stroke-width="1.4"/></svg>
        contact@harrowgateconstructionandmasonry.co.uk
      </p>
      <p class="contact-line">
        <svg class="contact-icon" viewBox="0 0 22 22"><circle cx="11" cy="11" r="11" fill="#00cc6f"/><circle cx="11" cy="11" r="5.8" fill="none" stroke="#0c1519" stroke-width="1.3"/><ellipse cx="11" cy="11" rx="2.6" ry="5.8" fill="none" stroke="#0c1519" stroke-width="1.2"/><path d="M5.2 11h11.6" stroke="#0c1519" stroke-width="1.2"/></svg>
        www.harrowgateconstructionandmasonry.co.uk
      </p>
    </section>

    <div class="social-square" aria-hidden="true"></div>
  </div>
</body>
</html>
```